Fixed price car insurance banner ad for insurance broker

We need a banner ad for addition to web pages and which will advertise an innovative insurance product we are selling.

We are an insurance broker and our product is a fixed price car insurance product.

The banner ad needs to display the company logo. This will be uploaded within the file upload section.

The remainder of the banner ad needs to explain what we are offering and also include the gear stick picture for impact.

We would like to see colours that tie in with the corporate colours, or alternative are striking and have presence on even the busiest web page I.e. Black banner and silver / white text. Please see the file upload for a sample of the brochure we are preparing for this product.

Target Market(s)

Private and commercial clients with both regular and high value motor vehicles.

Industry/Entity Type

Car Insurance

Font styles to use
Serif
Sans Serif

Colors

Designer to choose colors to be used in the design.

Requirements
Must have
• The banner must have the company logo on both pages.

I would like the advert to scroll / roll / fade or other between two pages displaying the following text:

Page 1
"Motor Insurance Scheme"
"Anything But Standard"
and including the gear knob picture

Page 2
Any Driver, Any Car, No Forms and One Flat Premium*

On clicking the banner ad, this will open an email, pre populated with email contact to request more detail.

Nice to have
• Open to your suggestions on this
Should not have
• Nothing at this stage. I will guide you when the ads are being submitted.

```html
<!DOCTYPE html>
<html lang="en">
<head>
<meta charset="utf-8">
<title>Halvern Insurance – Motor Insurance Banners</title>
<link rel="stylesheet" href="https://fonts.googleapis.com/css2?family=Tinos:wght@400;700&display=swap">
<style>
  :root {
    --page-bg: #ffffff;
    --frame-outer: #3b3f8f;
    --frame-inner: #c9ccd6;
    --silver-light: #f4f5f8;
    --silver-mid: #c3c8d2;
    --silver-dark: #8c93a1;
    --brand-ink: #1f2a6b;
    --band-black: #050506;
    --band-grey: #4a4d52;
    --band-sheen: #9a9ea5;
    --text-silver: #f1f2f4;
    --knob-light: #f2f2f2;
    --knob-dark: #8d9096;
  }
  html, body {
    margin: 0;
    padding: 0;
    width: 1200px;
    height: 577px;
    overflow: hidden;
    background: var(--page-bg);
  }
  .canvas {
    position: relative;
    width: 1200px;
    height: 577px;
    font-family: "Tinos", "Times New Roman", serif;
  }
  .banner {
    position: absolute;
    left: 42px;
    width: 1133px;
    height: 127px;
    box-sizing: border-box;
    border: 3px solid var(--frame-outer);
    outline: 2px solid var(--frame-inner);
    outline-offset: -6px;
    background: var(--band-black);
    overflow: hidden;
  }
  .banner--one { top: 42px; }
  .banner--two { top: 237px; }
  .banner--three { top: 433px; }

  .brand-panel {
    position: absolute;
    left: 0;
    top: 0;
    width: 230px;
    height: 100%;
    background: linear-gradient(160deg, var(--silver-light) 0%, var(--silver-mid) 55%, var(--silver-dark) 100%);
    display: flex;
    align-items: center;
    justify-content: center;
    text-align: center;
  }
  .brand-name {
    margin: 0;
    font-family: "Tinos", "Times New Roman", serif;
    font-weight: 700;
    font-size: 26px;
    line-height: 1.15;
    letter-spacing: 2px;
    color: var(--brand-ink);
    text-transform: uppercase;
  }

  .message-band {
    position: absolute;
    left: 230px;
    top: 0;
    right: 0;
    height: 100%;
    background:
      linear-gradient(165deg, transparent 0%, transparent 38%, rgba(154,158,165,0.55) 48%, transparent 60%),
      linear-gradient(90deg, var(--band-grey) 0%, var(--band-black) 35%, var(--band-black) 100%);
  }

  .message {
    position: absolute;
    left: 278px;
    width: 710px;
    top: 14px;
    margin: 0;
    color: var(--text-silver);
    font-size: 30px;
    line-height: 46px;
    font-weight: 400;
  }
  .message-line { display: block; white-space: nowrap; }
  .message-line--lead { text-align: left; }
  .message-line--follow { text-align: right; }
  .message sup { font-size: 16px; }

  .gear-knob {
    position: absolute;
    right: 22px;
    top: 6px;
    width: 112px;
    height: 112px;
    border-radius: 50%;
    background: radial-gradient(circle at 38% 35%, var(--knob-light) 0%, #d4d6da 50%, var(--knob-dark) 100%);
  }
</style>
</head>
<body>
<main class="canvas">

  <section class="banner banner--one">
    <div class="brand-panel"><p class="brand-name">Halvern<br>Insurance</p></div>
    <div class="message-band"></div>
    <p class="message">
      <span class="message-line message-line--lead">A Motor Insurance Plan that</span>
      <span class="message-line message-line--follow">is Anything But Standard</span>
    </p>
    <div class="gear-knob" role="img" aria-label="Silver gear stick knob showing the shift pattern 1 3 5, 2 4 R"></div>
  </section>

  <section class="banner banner--two">
    <div class="brand-panel"><p class="brand-name">Halvern<br>Insurance</p></div>
    <div class="message-band"></div>
    <p class="message">
      <span class="message-line message-line--lead">&nbsp;Any Driver, Any Car, No Forms</span>
      <span class="message-line message-line--follow">and One Flat Premium<sup>*</sup></span>
    </p>
    <div class="gear-knob" role="img" aria-label="Silver gear stick knob showing the shift pattern 1 3 5, 2 4 R"></div>
  </section>

  <section class="banner banner--three">
    <div class="brand-panel"><p class="brand-name">Halvern<br>Insurance</p></div>
    <div class="message-band"></div>
    <p class="message">
      <span class="message-line message-line--lead">Contact Dan Wexley at dan.wexley@harbrook.co</span>
      <span class="message-line message-line--follow">or Call 07700 900418&nbsp;&nbsp;&nbsp;&nbsp;&nbsp;&nbsp;</span>
    </p>
    <div class="gear-knob" role="img" aria-label="Silver gear stick knob showing the shift pattern 1 3 5, 2 4 R"></div>
  </section>

</main>
</body>
</html>
```